Rock band business card design

I need an edgy double sided business card to hand out at music events and to send out to radio.

It needs to display our logo, web address and social media icons (linkora, plumbit, vostramesh).

Colour scheme to match our website (www.thedrelliq.com)

Please include this quote:
The clock is turning... a reckoning... THE DRELLIQ.

Logo files have been attached.

I look forward to seeing your designs!

Target Market(s)

radio stations, music fans.

Industry/Entity Type

Events

Requirements
Must have
• Website address, social media icons, quote, colour scheme to match www.thedrelliq.com

```html
<!DOCTYPE html>
<html lang="en">
<head>
<meta charset="utf-8">
<title>The Drelliq – Business Card</title>
<link rel="stylesheet" href="https://fonts.googleapis.com/css2?family=Oswald:wght@300;400&display=swap">
<style>
  :root {
    --page-bg: #e4e2de;
    --card-black: #0b0b0b;
    --card-white: #f4f4f4;
    --ink-white: #f2f2f2;
    --ink-dark: #1a1a1a;
    --ghost-on-black: #2a2a2a;
    --ghost-on-white: #dcdcdc;
    --rule: #555555;
    --icon-plumbit: #2aa3dd;
    --icon-vostramesh: #3a3a3a;
    --icon-linkora: #3b5a98;
  }
  * { margin: 0; padding: 0; box-sizing: border-box; }
  html, body {
    width: 1200px; height: 900px; overflow: hidden;
    background: var(--page-bg);
    font-family: "Oswald", sans-serif;
  }
  .sheet {
    width: 1200px; height: 900px;
    display: flex; flex-direction: column; align-items: center; justify-content: center;
    gap: 40px;
  }
  .card {
    position: relative; width: 700px; height: 400px; overflow: hidden;
    box-shadow: 0 6px 18px rgba(0,0,0,0.18);
  }

  /* Front */
  .card--front { background: var(--card-black); color: var(--ink-white); }
  .front__mark {
    position: absolute; left: 50px; top: 60px;
    display: flex; align-items: center; gap: 14px;
  }
  .front__mark-dot { width: 16px; height: 16px; border-radius: 50%; background: var(--ink-white); }
  .front__mark-name {
    font-weight: 400; font-size: 40px; letter-spacing: 6px; text-transform: uppercase;
  }
  .front__ghost {
    position: absolute; right: -20px; bottom: 18px;
    font-weight: 400; font-size: 96px; letter-spacing: 10px; text-transform: uppercase;
    color: var(--ghost-on-black); white-space: nowrap;
  }
  .front__quote {
    position: absolute; left: 50px; top: 190px;
    list-style: none; font-weight: 300; font-size: 22px; letter-spacing: 5px;
    text-transform: uppercase; line-height: 46px;
  }
  .front__quote li:nth-child(2) { padding-left: 150px; }
  .front__quote li:nth-child(3) { padding-left: 300px; }

  /* Back */
  .card--back { background: var(--card-white); color: var(--ink-dark); }
  .back__ghost {
    position: absolute; left: 40px; top: 20px;
    font-weight: 400; font-size: 86px; letter-spacing: 10px; text-transform: uppercase;
    color: var(--ghost-on-white); white-space: nowrap;
  }
  .back__contacts {
    position: absolute; left: 60px; top: 150px; list-style: none;
  }
  .back__contact {
    display: flex; align-items: center; gap: 16px;
    font-weight: 400; font-size: 20px; letter-spacing: 5px; text-transform: uppercase;
    line-height: 40px;
  }
  .back__icon { width: 22px; height: 22px; }
  .back__icon--plumbit { background: var(--icon-plumbit); border-radius: 50%; }
  .back__icon--vostramesh { background: var(--icon-vostramesh); }
  .back__icon--linkora { background: var(--icon-linkora); }
  .back__network { width: 130px; font-size: 16px; letter-spacing: 3px; }
  .back__rule { width: 560px; height: 1px; background: var(--rule); margin: 14px 0 10px; }
  .back__web {
    font-weight: 400; font-size: 22px; letter-spacing: 6px; text-transform: uppercase;
  }
</style>
</head>
<body>
<main class="sheet">
  <section class="card card--front" aria-label="Card front">
    <div class="front__ghost" aria-hidden="true">The Drelliq</div>
    <div class="front__mark">
      <span class="front__mark-dot"></span>
      <span class="front__mark-name">The Drelliq</span>
    </div>
    <ul class="front__quote">
      <li>The clock is turning...</li>
      <li>a reckoning...</li>
      <li>The Drelliq.</li>
    </ul>
  </section>

  <section class="card card--back" aria-label="Card back">
    <div class="back__ghost" aria-hidden="true">The Drelliq</div>
    <ul class="back__contacts">
      <li class="back__contact"><span class="back__icon back__icon--plumbit"></span><span class="back__network">plumbit</span>@ thedrelliq</li>
      <li class="back__contact"><span class="back__icon back__icon--vostramesh"></span><span class="back__network">vostramesh</span>@ thedrelliq</li>
      <li class="back__contact"><span class="back__icon back__icon--linkora"></span><span class="back__network">linkora</span>thedrelliq</li>
      <li><div class="back__rule"></div></li>
      <li class="back__web">www.thedrelliq.com</li>
    </ul>
  </section>
</main>
</body>
</html>
```